Meadowlark Learning Growth Partners (MLGP)

This is a professional business card. Logo and picture are a must on the front of the card. I am an educational consultant. I have been consulting for the past three years for a company. I am now opening my own company. My goal for my consulting company is to eventually consult all over America.

Target Market(s)

Educators, schools, professionals

Industry/Entity Type

Consulting

Contact Information for Business Card

Picture/logo on front, simple modern design

Font styles to use
Serif

Colors
85abd2
0355a3
3176b5
cedeed

Requirements
Must have
• picture, logo,
• Odessa Pruitt, Ed.S
• address 5073 Cormorant ridge Dr. Nashville, TN 37940
• Cell:616-555-0148
• Office: 629-555-0172
• www.Mlgpedu.example
• pruittodessa@mailbox.example

```html
<!DOCTYPE html>
<html lang="en">
<head>
<meta charset="utf-8">
<title>Meadowlark Learning Growth Partners — Business Card</title>
<link href="https://fonts.googleapis.com/css2?family=Montserrat:wght@700&family=Roboto:wght@400;500&display=swap" rel="stylesheet">
<style>
  :root {
    --backdrop: #2a2a2c;
    --card: #ffffff;
    --navy: #0b3b80;
    --navy-deep: #083270;
    --white: #ffffff;
  }
  * { box-sizing: border-box; margin: 0; padding: 0; }
  html, body { width: 1200px; height: 900px; overflow: hidden; }
  body { background: var(--backdrop); position: relative; font-family: "Roboto", Arial, sans-serif; }

  .card {
    position: absolute; left: 250px; width: 700px; height: 400px;
    background: var(--card); border-radius: 18px; overflow: hidden;
    box-shadow: 0 14px 30px rgba(0,0,0,.55);
  }
  .card--front { top: 40px; }
  .card--back { top: 460px; }
  .card__swoosh { position: absolute; inset: 0; width: 100%; height: 100%; }

  /* front */
  .brand-mark {
    position: absolute; top: 95px; left: 0; right: 0;
    display: flex; align-items: center; justify-content: center; gap: 14px;
    font-family: "Montserrat", Arial, sans-serif; font-weight: 700;
    font-size: 64px; letter-spacing: 4px; color: var(--navy);
  }
  .brand-mark__dot { width: 30px; height: 30px; border-radius: 50%; background: var(--navy); }
  .front-web {
    position: absolute; left: 60px; bottom: 28px;
    color: var(--white); font-size: 17px; letter-spacing: .5px;
  }

  /* back */
  .portrait {
    position: absolute; left: 72px; top: 78px; width: 160px; height: 160px;
    border: 4px solid var(--navy);
    background: linear-gradient(160deg, #4f7fc4 0%, #3a68ad 55%, #1f2a3d 100%);
  }
  .person { position: absolute; left: 42px; top: 250px; width: 220px; text-align: center; color: var(--navy); }
  .person__name { font-family: "Montserrat", Arial, sans-serif; font-weight: 700; font-size: 21px; }
  .person__title { font-size: 14px; margin-top: 2px; }

  .lockup {
    position: absolute; left: 372px; top: 36px;
    display: flex; align-items: center; gap: 12px; color: var(--navy);
  }
  .lockup__dot { width: 22px; height: 22px; border-radius: 50%; background: var(--navy); }
  .lockup__short { font-family: "Montserrat", Arial, sans-serif; font-weight: 700; font-size: 28px; letter-spacing: 3px; }
  .lockup__rule { width: 1.5px; height: 66px; background: var(--navy); }
  .lockup__full { font-family: "Montserrat", Arial, sans-serif; font-weight: 700; font-size: 13px; line-height: 16px; }

  .contact {
    position: absolute; right: 36px; top: 200px;
    list-style: none; color: var(--white); font-size: 15px; text-align: right;
  }
  .contact__item { display: flex; justify-content: flex-end; align-items: center; gap: 10px; height: 27px; }
  .contact__item svg { width: 14px; height: 14px; fill: var(--white); flex: none; }
</style>
</head>
<body>

<section class="card card--front">
  <svg class="card__swoosh" viewBox="0 0 700 400" aria-hidden="true">
    <path d="M0,400 L0,322 C160,250 330,232 480,212 C585,196 655,140 700,96 L700,400 Z" fill="var(--navy)"/>
    <path d="M520,205 C610,180 668,130 700,100 L700,118 C660,150 600,190 520,205 Z" fill="var(--navy-deep)"/>
    <path d="M60,335 C200,270 380,255 520,232 C610,216 670,170 700,140" fill="none" stroke="var(--white)" stroke-width="3"/>
    <path d="M520,210 C610,190 665,145 700,112" fill="none" stroke="var(--white)" stroke-width="2"/>
  </svg>
  <div class="brand-mark"><span class="brand-mark__dot"></span>MLGP</div>
  <p class="front-web">www.Mlgpedu.example</p>
</section>

<section class="card card--back">
  <svg class="card__swoosh" viewBox="0 0 700 400" aria-hidden="true">
    <path d="M0,400 L0,318 C150,345 285,318 385,240 C480,165 575,115 700,88 L700,400 Z" fill="var(--navy)"/>
    <path d="M0,342 C160,360 290,330 390,255" fill="none" stroke="var(--white)" stroke-width="4"/>
    <path d="M0,356 C170,372 300,345 400,268" fill="none" stroke="var(--white)" stroke-width="2"/>
    <path d="M440,190 C530,140 600,112 680,100" fill="none" stroke="var(--white)" stroke-width="2"/>
  </svg>

  <div class="portrait" role="img" aria-label="Portrait photo of Odessa Pruitt"></div>
  <div class="person">
    <p class="person__name">Odessa Pruitt</p>
    <p class="person__title">Ed.S</p>
  </div>

  <div class="lockup">
    <span class="lockup__dot"></span>
    <span class="lockup__short">MLGP</span>
    <span class="lockup__rule"></span>
    <span class="lockup__full">Meadowlark<br>Learning<br>Growth<br>Partners</span>
  </div>

  <ul class="contact">
    <li class="contact__item">616-555-0148
      <svg viewBox="0 0 24 24"><path d="M6.6 10.8a15 15 0 0 0 6.6 6.6l2.2-2.2a1 1 0 0 1 1-.25 11.4 11.4 0 0 0 3.6.57 1 1 0 0 1 1 1V20a1 1 0 0 1-1 1A17 17 0 0 1 3 4a1 1 0 0 1 1-1h3.5a1 1 0 0 1 1 1c0 1.25.2 2.45.57 3.57a1 1 0 0 1-.25 1z"/></svg></li>
    <li class="contact__item">629-555-0172
      <svg viewBox="0 0 24 24"><path d="M2 8c5-5 15-5 20 0l-3 3-4-2V7H9v2l-4 2zM6 13h12l2 8H4z"/></svg></li>
    <li class="contact__item">pruittodessa@mailbox.example
      <svg viewBox="0 0 24 24"><path d="M2 5h20v14H2zm2 2v.5l8 5 8-5V7zm0 3v7h16v-7l-8 5z"/></svg></li>
    <li class="contact__item">www.Mlgpedu.example
      <svg viewBox="0 0 24 24"><path d="M12 2a10 10 0 1 0 0 20 10 10 0 0 0 0-20zm0 2a8 8 0 0 1 7.7 6H15a14 14 0 0 0-2-5.9zm-2.9.5A14 14 0 0 0 9 10H4.3a8 8 0 0 1 4.8-5.5zM4.3 14H9a14 14 0 0 0 1 5.5A8 8 0 0 1 4.3 14zm6.7 0h2a12 12 0 0 1-1 4.5 12 12 0 0 1-1-4.5zm0-4a12 12 0 0 1 1-4.5 12 12 0 0 1 1 4.5zm4 4h4.7a8 8 0 0 1-4.8 5.5A14 14 0 0 0 15 14z"/></svg></li>
    <li class="contact__item">5073 Cormorant ridge Dr. Nashville, TN 37940
      <svg viewBox="0 0 24 24"><path d="M12 2a7 7 0 0 0-7 7c0 5 7 13 7 13s7-8 7-13a7 7 0 0 0-7-7zm0 9.5a2.5 2.5 0 1 1 0-5 2.5 2.5 0 0 1 0 5z"/></svg></li>
  </ul>
</section>

</body>
</html>
```